New Business Card Design Project

hello again,
i have an awful year and we were not able to complete our logo plan. we would like to use our #1 logo for business card design process. the primary colors for business card should be white background with orange & black letters. our business is mobil truck cranes. we deliver heavy stuff and unload cargo with crane that is mounted on our trucks.
here is our business card info:
HARBOR LIFT HAULERS, INC.
428 WESTCOTT AVE
MERRICK, NY 11542
OFFICE - 516 487 3091
DIRECT - 1 888 LIFT HAULS
MARK@HLHAULERS.COM
PLEASE also try to get our slogan on card .... "Our Loads Keep Rollin"
lastly please also put "24 hour Knuckleboom Service"
you can call me anytime 24/7 to discuss...my cell # is: 516 759 2036
please also list: Mark Delroy, President
Target Market(s)
Heavy Construction industry
Industry/Entity Type
heavy construction industry
Contact Information for Business Card
24 Hr Knuckleboom Service

```html
<!DOCTYPE html>
<html lang="en">
<head>
<meta charset="utf-8">
<title>Harbor Lift Haulers – Business Card</title>
<link href="https://fonts.googleapis.com/css2?family=Montserrat:wght@400;500;600;700;800&display=swap" rel="stylesheet">
<style>
  :root {
    --orange: #f47f24;
    --orange-deep: #ee6f1a;
    --ink: #1b1b1b;
    --paper: #ffffff;
    --backdrop: #c9cccd;
  }
  * { margin: 0; padding: 0; box-sizing: border-box; }
  html, body {
    width: 1187px; height: 1200px; overflow: hidden;
    background: var(--backdrop);
    font-family: "Montserrat", sans-serif;
  }
  .canvas { position: relative; width: 1187px; height: 1200px; }
  .card { position: absolute; left: 207px; width: 773px; height: 445px; }
  .card-front { top: 114px; background: var(--orange); color: var(--paper); }
  .card-back { top: 639px; background: var(--paper); color: var(--ink); }

  .front-slogan {
    position: absolute; left: 0; right: 0; top: 150px; text-align: center;
    font-weight: 800; font-size: 34px; letter-spacing: 1px; text-transform: uppercase;
  }
  .front-mark {
    position: absolute; left: 0; right: 0; top: 250px;
    display: flex; align-items: center; justify-content: center; gap: 14px;
  }
  .front-mark .mark-square { width: 30px; height: 30px; background: var(--paper); }
  .front-mark .brand-name { font-weight: 800; font-size: 40px; letter-spacing: 0.5px; }
  .front-tagline {
    position: absolute; left: 0; right: 0; top: 360px; text-align: center;
    font-weight: 700; font-size: 22px; letter-spacing: 1px;
  }

  .back-slogan {
    position: absolute; left: 450px; top: 62px; width: 290px;
    font-weight: 800; font-size: 18px; letter-spacing: 0.5px; text-transform: uppercase;
    color: var(--ink);
  }
  .back-mark {
    position: absolute; left: 450px; top: 112px; width: 290px;
    display: flex; align-items: center; gap: 10px;
  }
  .back-mark .mark-square { width: 20px; height: 20px; background: var(--orange); flex: none; }
  .back-mark .brand-name { font-weight: 800; font-size: 24px; color: var(--ink); line-height: 1.1; }

  .holder { position: absolute; left: 37px; top: 193px; }
  .holder-name { color: var(--orange); font-weight: 700; font-size: 30px; letter-spacing: 1.5px; line-height: 1.1; }
  .holder-title { font-size: 17px; letter-spacing: 1.5px; font-weight: 500; margin-top: 2px; }

  .address { position: absolute; left: 37px; top: 333px; font-size: 17px; letter-spacing: 1px; line-height: 23px; font-weight: 500; font-style: normal; }
  .address .company { color: var(--orange); font-weight: 600; }

  .contacts { position: absolute; left: 450px; top: 281px; list-style: none; font-size: 17px; letter-spacing: 1.5px; font-weight: 500; }
  .contacts li { display: flex; align-items: center; gap: 8px; height: 32px; }
  .contacts svg { width: 13px; height: 13px; fill: var(--orange); flex: none; }

  .base-line { position: absolute; left: 0; right: 0; top: 427px; height: 3px; background: var(--ink); }
  .base-band { position: absolute; left: 0; right: 0; top: 430px; height: 15px; background: var(--orange-deep); }
</style>
</head>
<body>
<div class="canvas">
  <section class="card card-front">
    <p class="front-slogan">“Our Loads Keep Rollin”</p>
    <div class="front-mark">
      <span class="mark-square"></span>
      <span class="brand-name">HARBOR LIFT HAULERS INC</span>
    </div>
    <p class="front-tagline">24 hour Knuckleboom Service</p>
  </section>

  <section class="card card-back">
    <p class="back-slogan">“Our Loads Keep Rollin”</p>
    <div class="back-mark">
      <span class="mark-square"></span>
      <span class="brand-name">HARBOR LIFT HAULERS INC</span>
    </div>

    <div class="holder">
      <p class="holder-name">MARK DELROY</p>
      <p class="holder-title">PRESIDENT</p>
    </div>

    <address class="address">
      <div class="company">HARBOR LIFT HAULERS, INC.</div>
      <div>428 WESTCOTT AVE</div>
      <div>MERRICK, NY 11542</div>
    </address>

    <ul class="contacts">
      <li><svg viewBox="0 0 16 16"><path d="M3 1l3 3-1.5 2c1 2 3 4 5 5L11.5 9.5l3 3-2 2.5C7 14 2 9 1 3z"/></svg>516 487 3091</li>
      <li><svg viewBox="0 0 16 16"><path d="M3 1l3 3-1.5 2c1 2 3 4 5 5L11.5 9.5l3 3-2 2.5C7 14 2 9 1 3z"/></svg>1 888 LIFT HAULS</li>
      <li><svg viewBox="0 0 16 16"><path d="M1 6l7-5 7 5v9H1z M2.5 6.5L8 10l5.5-3.5"/></svg>MARK@HLHAULERS.COM</li>
      <li><svg viewBox="0 0 16 16"><circle cx="8" cy="8" r="7"/><path d="M1 8h14M8 1v14" stroke="#fff" stroke-width="1.2"/></svg>WWW.HLHAULERS.COM</li>
    </ul>

    <div class="base-line"></div>
    <div class="base-band"></div>
  </section>
</div>
</body>
</html>
```